Modern Business Card for Lanternfield 2018

Our company assumes the best about people. We are creating an online community of entrepreneurs and business leaders who struggle with marketing their business online.

This business card should POP! We recently got a new logo and are launching a new website next month, so our business cards should make a statement that feels:
-Fresh
-Smart
-Trustworthy
-Fun

Target Market(s)

small business owners, entrepreneurs

Industry/Entity Type

Digital Marketing

Contact Information for Business Card

Dimensions: 3.5" x 2"

Font styles to use
Sans Serif

Colors
f37122
ffffff

Requirements
Must have
• We need a business card with a modern, bold design. We will use one side of the card as a lead-generation offer, so text on one side will need to fit up to 140 characters. The business card should stick to our core colors (orange, black, and white).
Nice to have
• We think a vertical "portrait" design could be interesting.
Should not have
• Should not look like a traditional business card. The round icon should stand out from a distance.

```html
<!DOCTYPE html>
<html lang="en">
<head>
<meta charset="utf-8">
<title>Lanternfield Business Card</title>
<link href="https://fonts.googleapis.com/css2?family=Open+Sans:wght@400;600;700;800&display=swap" rel="stylesheet">
<style>
  :root {
    --orange: #f37122;
    --white: #ffffff;
    --black: #1a1a1a;
    --grey: #555555;
    --faint-orange: #fbe3d6;
    --stage: #e9e9e9;
    --line: rgba(255,255,255,0.45);
  }
  * { margin: 0; padding: 0; box-sizing: border-box; }
  html, body { width: 1200px; height: 960px; overflow: hidden; }
  body {
    background: var(--stage);
    font-family: "Open Sans", Arial, sans-serif;
    position: relative;
  }
  .card {
    position: absolute;
    left: 250px;
    width: 700px;
    height: 400px;
    overflow: hidden;
    box-shadow: 0 8px 24px rgba(0,0,0,0.18);
  }
  /* Offer side */
  .card--offer { top: 50px; background: var(--orange); color: var(--white); }
  .offer__mark {
    position: absolute; left: 60px; top: 50px;
    width: 190px; height: 190px; border-radius: 50%;
    background: var(--white);
  }
  .offer__divider {
    position: absolute; left: 300px; top: 40px;
    width: 2px; height: 220px; background: var(--line);
  }
  .offer__copy { position: absolute; left: 330px; top: 44px; width: 345px; }
  .offer__headline {
    font-weight: 800; font-size: 24px; line-height: 1.1;
    text-transform: uppercase; letter-spacing: 0.2px;
  }
  .offer__body { font-size: 18px; line-height: 1.3; margin-top: 10px; opacity: 0.92; }
  .offer__url { font-weight: 700; font-size: 20px; margin-top: 12px; }
  .offer__notes {
    position: absolute; left: 40px; right: 30px; top: 282px; height: 86px;
    background: var(--white); border-radius: 18px;
    padding: 26px 28px 0;
  }
  .offer__rule { height: 1px; background: #555; margin-bottom: 26px; }

  /* Contact side */
  .card--contact { top: 510px; background: var(--white); }
  .contact__watermark {
    position: absolute; left: 20px; top: 110px;
    width: 310px; height: 310px; border-radius: 50%;
    background: var(--faint-orange); opacity: 0.7;
  }
  .contact__person { position: absolute; left: 55px; top: 180px; }
  .contact__name { color: var(--orange); font-weight: 700; font-size: 24px; text-transform: uppercase; }
  .contact__role { color: var(--black); font-weight: 700; font-size: 18px; text-transform: uppercase; margin-top: 2px; }
  .contact__email { color: var(--grey); font-size: 17px; margin-top: 2px; }
  .brand { position: absolute; right: 40px; top: 80px; width: 310px; text-align: center; }
  .brand__dot {
    width: 28px; height: 28px; border-radius: 50%;
    background: var(--orange); margin: 0 auto 8px;
  }
  .brand__name {
    color: var(--black); font-weight: 800; font-size: 34px;
    letter-spacing: 1px; text-transform: uppercase; line-height: 1;
  }
  .brand__tagline {
    color: var(--black); font-weight: 700; font-size: 13px;
    letter-spacing: 1.2px; text-transform: uppercase; margin-top: 8px;
  }
</style>
</head>
<body>
  <section class="card card--offer">
    <div class="offer__mark"></div>
    <div class="offer__divider"></div>
    <div class="offer__copy">
      <p class="offer__headline">Grow your audience.<br>Earn more revenue.<br>Build real momentum.</p>
      <p class="offer__body">Claim your free Lanternfield Launch Kit and our marketing guide today at</p>
      <p class="offer__url">Lanternfieldnow.com/start</p>
    </div>
    <div class="offer__notes">
      <div class="offer__rule"></div>
      <div class="offer__rule"></div>
    </div>
  </section>

  <section class="card card--contact">
    <div class="contact__watermark"></div>
    <div class="contact__person">
      <p class="contact__name">Dana Whitlock</p>
      <p class="contact__role">Story Marketing Coach</p>
      <p class="contact__email">dana@lanternfieldnow.com</p>
    </div>
    <div class="brand">
      <div class="brand__dot"></div>
      <p class="brand__name">Lanternfield</p>
      <p class="brand__tagline">Share stories that move people</p>
    </div>
  </section>
</body>
</html>
```